Full Page Appliance Ad

Create a full page ad (7.5" W x 10" H) representing that we are a full service appliance company, where we have a showroom located at 14 N. Birch Lane Souderton, PA 18970. Our website is www.qrtolvek.com , and our phone number is 215-555-0148. We don't only sell appliances, we deliver, install, and service. We also offer an additional year warranty* (see store for details). In addition to appliances, we also have an Electrical Department that specializes in residential applications.
May be best if split the full page ad into two spots. One spot to reference appliances, and the other to represent electrical.
I want it to look clean, and not too busy
Target Market(s)
30-70 years old
Look and feel

```html
<!DOCTYPE html>
<html lang="en">
<head>
<meta charset="utf-8">
<title>Qrtolvek and Son Inc — Appliances Services</title>
<link rel="stylesheet" href="https://fonts.googleapis.com/css2?family=Anton&family=Montserrat:wght@600;700;800&family=Roboto:wght@400&display=swap">
<style>
  :root {
    --paper: #ececee;
    --navy: #1c2150;
    --royal: #2a72bd;
    --white: #ffffff;
    --steel-light: #d9dadd;
    --steel-dark: #8d9096;
    --photo-blue: #3a7bd0;
    --photo-white: #e9e9ec;
  }
  * { margin: 0; padding: 0; box-sizing: border-box; }
  html, body { width: 900px; height: 1200px; overflow: hidden; }
  body { background: var(--paper); font-family: "Montserrat", sans-serif; }
  .ad { position: relative; width: 900px; height: 1200px; overflow: hidden; background: linear-gradient(180deg, #f1f1f3 0%, #e8e8ea 100%); }

  .brand-mark { position: absolute; left: 55px; top: 29px; width: 94px; height: 94px; border-radius: 50%; border: 6px solid var(--navy); }
  .brand-name { position: absolute; left: 159px; top: 42px; font-weight: 700; color: var(--navy); text-transform: uppercase; line-height: 1; }
  .brand-name .name-main { display: block; font-size: 30px; letter-spacing: 0.5px; }
  .brand-name .name-sub { display: block; font-size: 23px; margin-top: 6px; letter-spacing: 0.5px; }

  .website { position: absolute; right: 53px; top: 58px; font-weight: 700; font-size: 19px; line-height: 1; letter-spacing: 1.8px; color: var(--navy); }

  .appliance-photo { position: absolute; left: 556px; top: 217px; width: 344px; height: 370px; background: linear-gradient(160deg, var(--steel-light) 0%, #b9bbbf 55%, var(--steel-dark) 100%); border-radius: 6px 0 0 6px; }

  .headline { font-family: "Anton", sans-serif; font-weight: 400; text-transform: uppercase; }
  .headline span { position: absolute; left: 52px; line-height: 1; transform-origin: left top; white-space: nowrap; }
  .headline .line-appliances { top: 190px; font-size: 102px; color: var(--royal); transform: scaleX(1.1); }
  .headline .line-services { top: 285px; font-size: 112px; color: var(--navy); transform: scaleX(1.08); }

  .offer-list { position: absolute; left: 55px; top: 407px; list-style: none; }
  .offer-list li { display: flex; align-items: center; gap: 13px; height: 41px; line-height: 41px; font-weight: 800; font-size: 34px; color: var(--navy); text-transform: uppercase; }
  .offer-list svg { width: 26px; height: 26px; flex: none; }

  .electric-band { position: absolute; left: 0; top: 0; width: 900px; height: 1200px; }

  .tech-photo { position: absolute; left: 500px; top: 578px; width: 400px; height: 622px; background: linear-gradient(180deg, var(--photo-blue) 0%, var(--photo-blue) 22%, var(--photo-white) 40%, #cfd3dc 70%, var(--photo-blue) 100%); border-radius: 120px 0 0 0; }

  .electric-title { position: absolute; left: 52px; top: 668px; font-weight: 800; font-size: 47px; line-height: 49px; color: var(--white); text-transform: uppercase; }

  .electric-list { position: absolute; left: 52px; top: 775px; list-style: none; font-family: "Roboto", sans-serif; color: var(--white); font-size: 28px; }
  .electric-list li { display: flex; align-items: center; gap: 6px; height: 32.3px; line-height: 32.3px; white-space: nowrap; }
  .electric-list svg { width: 18px; height: 18px; flex: none; }
  .electric-list .more { padding-left: 24px; }

  .call-label { position: absolute; left: 52px; top: 1023px; font-weight: 800; font-size: 28px; line-height: 1; color: var(--white); text-transform: uppercase; }
  .call-number { position: absolute; left: 51px; top: 1047px; font-weight: 800; font-size: 43px; line-height: 1; color: var(--white); letter-spacing: -0.5px; }

  .address { position: absolute; left: 52px; top: 1121px; display: flex; align-items: center; gap: 8px; color: var(--white); font-style: normal; font-weight: 600; font-size: 18px; line-height: 20px; }
  .address svg { width: 26px; height: 34px; flex: none; }
</style>
</head>
<body>
<main class="ad">

  <header>
    <span class="brand-mark" aria-hidden="true"></span>
    <p class="brand-name"><span class="name-main">Qrtolvek</span><span class="name-sub">and Son Inc</span></p>
    <p class="website">www.qrtolvek.com</p>
  </header>

  <section class="appliances" aria-label="Appliance services">
    <div class="appliance-photo" role="img" aria-label="Group of stainless steel kitchen appliances: refrigerators, dishwasher, oven, washer, microwave, blender and coffee machine"></div>
    <h1 class="headline">
      <span class="line-appliances">Appliances</span>
      <span class="line-services">Services</span>
    </h1>
    <ul class="offer-list">
      <li><svg viewBox="0 0 24 24" aria-hidden="true"><circle cx="11" cy="13" r="9" fill="none" stroke="#2a72bd" stroke-width="2.6"/><path d="M6.5 12.5l4 4L21 5" fill="none" stroke="#2a72bd" stroke-width="2.8" stroke-linecap="round" stroke-linejoin="round"/></svg>Seller</li>
      <li><svg viewBox="0 0 24 24" aria-hidden="true"><circle cx="11" cy="13" r="9" fill="none" stroke="#2a72bd" stroke-width="2.6"/><path d="M6.5 12.5l4 4L21 5" fill="none" stroke="#2a72bd" stroke-width="2.8" stroke-linecap="round" stroke-linejoin="round"/></svg>Deliver</li>
      <li><svg viewBox="0 0 24 24" aria-hidden="true"><circle cx="11" cy="13" r="9" fill="none" stroke="#2a72bd" stroke-width="2.6"/><path d="M6.5 12.5l4 4L21 5" fill="none" stroke="#2a72bd" stroke-width="2.8" stroke-linecap="round" stroke-linejoin="round"/></svg>Installation</li>
      <li><svg viewBox="0 0 24 24" aria-hidden="true"><circle cx="11" cy="13" r="9" fill="none" stroke="#2a72bd" stroke-width="2.6"/><path d="M6.5 12.5l4 4L21 5" fill="none" stroke="#2a72bd" stroke-width="2.8" stroke-linecap="round" stroke-linejoin="round"/></svg>Maintenance</li>
    </ul>
  </section>

  <section class="electrical" aria-label="Electrical department">
    <svg class="electric-band" viewBox="0 0 900 1200" aria-hidden="true">
      <defs>
        <linearGradient id="bandFill" x1="0" y1="1" x2="1" y2="0">
          <stop offset="0" stop-color="#2d6cb3"/>
          <stop offset="0.6" stop-color="#23356e"/>
          <stop offset="1" stop-color="#1f2a5e"/>
        </linearGradient>
      </defs>
      <path d="M0 652 C 140 585, 390 560, 560 625 C 720 690, 840 790, 900 920 L 900 1200 L 0 1200 Z" fill="url(#bandFill)"/>
    </svg>

    <div class="tech-photo" role="img" aria-label="Smiling electrician in a blue hard hat and overalls holding two wrenches"></div>

    <h2 class="electric-title">Need an<br>Electricien?</h2>

    <ul class="electric-list">
      <li><svg viewBox="0 0 24 24" aria-hidden="true"><circle cx="11" cy="13" r="9" fill="none" stroke="#fff" stroke-width="2.6"/><path d="M6.5 12.5l4 4L21 5" fill="none" stroke="#fff" stroke-width="2.8" stroke-linecap="round" stroke-linejoin="round"/></svg>Troubleshooting</li>
      <li><svg viewBox="0 0 24 24" aria-hidden="true"><circle cx="11" cy="13" r="9" fill="none" stroke="#fff" stroke-width="2.6"/><path d="M6.5 12.5l4 4L21 5" fill="none" stroke="#fff" stroke-width="2.8" stroke-linecap="round" stroke-linejoin="round"/></svg>Service Upgrades</li>
      <li><svg viewBox="0 0 24 24" aria-hidden="true"><circle cx="11" cy="13" r="9" fill="none" stroke="#fff" stroke-width="2.6"/><path d="M6.5 12.5l4 4L21 5" fill="none" stroke="#fff" stroke-width="2.8" stroke-linecap="round" stroke-linejoin="round"/></svg>Kitchen Remodels</li>
      <li><svg viewBox="0 0 24 24" aria-hidden="true"><circle cx="11" cy="13" r="9" fill="none" stroke="#fff" stroke-width="2.6"/><path d="M6.5 12.5l4 4L21 5" fill="none" stroke="#fff" stroke-width="2.8" stroke-linecap="round" stroke-linejoin="round"/></svg>Under Cabinet Lighting</li>
      <li><svg viewBox="0 0 24 24" aria-hidden="true"><circle cx="11" cy="13" r="9" fill="none" stroke="#fff" stroke-width="2.6"/><path d="M6.5 12.5l4 4L21 5" fill="none" stroke="#fff" stroke-width="2.8" stroke-linecap="round" stroke-linejoin="round"/></svg>Surge Protection</li>
      <li><svg viewBox="0 0 24 24" aria-hidden="true"><circle cx="11" cy="13" r="9" fill="none" stroke="#fff" stroke-width="2.6"/><path d="M6.5 12.5l4 4L21 5" fill="none" stroke="#fff" stroke-width="2.8" stroke-linecap="round" stroke-linejoin="round"/></svg>Celling Fan Installation</li>
      <li class="more">And More!</li>
    </ul>

    <p class="call-label">Give us a call</p>
    <p class="call-number">215-555-0148</p>

    <address class="address">
      <svg viewBox="0 0 24 32" aria-hidden="true"><path d="M12 1C5.9 1 1 5.9 1 12c0 8 11 19 11 19s11-11 11-19C23 5.9 18.1 1 12 1z" fill="#fff"/><circle cx="12" cy="12" r="4.5" fill="#2d6cb3"/></svg>
      <span>14 N. Birch Lane<br>Souderton, PA 18970.</span>
    </address>
  </section>

</main>
</body>
</html>
```